Design für ein Flyer mit Gutschein-Abriss
Zielgruppe
Handgemachte/ handgefertigte Körperpflege- und Kosmetikprodukte, die in kleinen Chargen gefertigt werden (somit wechselnde Produkte, die in bestimmten Mengen verfügbar sind) u.a. Seifen, Rasierseifen, Badezusätze, Gesichtspflege usw.
Die Produkte werden ohne künstliche Zusätze und Konservierungsstoffe hergestellt und erhalten so wenig Allergene-Stoffe wie möglich, zum Teil vegan.
In geringem Umfang werden ebenfalls Zubehör für Körperpflege vermarktet (z.B. Lavastein für Hornhautentfernung etc.).
Die Produkte werden online und im stationären Handel vertrieben.
Ansprechen von möglichst allen Altersgruppen.
Zielgruppe: 'Otto-Normal-Verbraucher', FRAUEN, Eltern (Mutter-Kind), Männer, in geringem Umfang Haustierbesitzer (Hundeshampoos etc.)
Aufgabenstellung
Größe: DinA5
Wir führen folgende Produkte in unserer Manufaktur:
Natürliche handgefertigte Naturseifen (Milchseifen, Kräuterseifen, Aromaseifen, uvm.), Seifentorten, Seifen- und Badecupcakes, handgerollte Badetrüffel, Badesalz, Badeöle, Badeeis, Badefondant, Körper- und Gesichtspflegeprodukte, Badezubehör, Aromatherapie, Dekorationsartikel sowie Geschenkkörbe für Privat- und Firmenkunden.
Die Produkte enthalten natürliche Inhaltsstoffe, zum Teil hochwertige ätherische Öle und sind Paraben- und SLS-frei. Unsere Produkte werden nicht an Tieren getestet. Wir achten bei der Auswahl der Inhaltsstoffe und unseren Lieferanten auf fairen Handel und nachhaltige Produktion.
Des Weiteren führen wir handgemachte Sojawachskerzen, diese sind Paraffin frei und enthalten Sojawachs aus nachhaltiger Produktion.
Der Flyer soll am unteren Rand den Gutschein beinhalten, welches abgeschnitten werden kann (mit 20 % Rabatt gilt für Online und im Laden).
Auf den Flyer sollten auf jeden Fall noch folgende Daten:
Neueröffnung am 05.05.2017
www.quorvablends.de
Öffnungszeiten: Freitags von 11:00 bis 18:00 Uhr
Anbei unser Logo so wie ein Link mit Bildern einiger unserer Produkte.
https://www.filekiste-beispiel.de/s/x71tq9wpzd3k0m/BBR4uKoLmTZ8wPaYc3nH7Vxe?dl=0
Wir freuen uns schon auf viele tolle Vorschläge.

```html
<!DOCTYPE html>
<html lang="de">
<head>
<meta charset="utf-8">
<title>Quorva Blends – Flyer mit Gutschein</title>
<link rel="stylesheet" href="https://fonts.googleapis.com/css2?family=Open+Sans:wght@300;400;600;700&family=Fredoka:wght@500;600&display=swap">
<style>
  :root {
    --green: #9aba2c;
    --green-light: #a9c63f;
    --green-soft: #b4cd55;
    --text: #4d4d4d;
    --text-soft: #5c5c5c;
    --white: #ffffff;
    --paper: #ffffff;
  }
  * { margin: 0; padding: 0; box-sizing: border-box; }
  html, body {
    width: 847px; height: 1200px; overflow: hidden;
    background: var(--paper);
  }
  .flyer {
    position: relative;
    width: 847px; height: 1200px;
    overflow: hidden;
    background: var(--paper);
    font-family: "Open Sans", Arial, sans-serif;
    color: var(--text);
  }
  .brand {
    position: absolute;
    right: 22px; top: 18px;
    width: 262px;
    text-align: center;
    color: var(--green);
  }
  .brand__name {
    display: flex; align-items: center; justify-content: center; gap: 12px;
    font-size: 40px; font-weight: 600; letter-spacing: 1px;
    line-height: 1.05;
  }
  .brand__dot {
    width: 18px; height: 18px; border-radius: 50%;
    background: var(--green);
    flex: none;
  }
  .brand__tagline {
    margin-top: 14px;
    font-size: 11px; font-weight: 600; letter-spacing: 0.6px;
    line-height: 14px;
    color: var(--text);
  }
  .product-photo {
    position: absolute;
    left: 0; top: 157px;
    width: 847px; height: 281px;
    background:
      radial-gradient(ellipse at 12% 60%, #f4d9dc 0%, transparent 45%),
      radial-gradient(ellipse at 35% 55%, #b0566a 0%, transparent 30%),
      radial-gradient(ellipse at 58% 45%, #e9d9c8 0%, transparent 35%),
      radial-gradient(ellipse at 78% 60%, #f5e79a 0%, transparent 30%),
      radial-gradient(ellipse at 93% 55%, #f6c7c7 0%, transparent 35%),
      linear-gradient(180deg, #ececec 0%, #f3eeee 100%);
  }
  .intro {
    position: absolute;
    left: 38px; top: 462px;
  }
  .intro__headline {
    font-size: 30px; font-weight: 600; color: var(--text);
    letter-spacing: 0.2px;
  }
  .intro__sub {
    margin-top: 8px;
    font-size: 28px; font-weight: 300; color: var(--text-soft);
  }
  .intro__basis {
    position: absolute;
    left: 38px; top: 580px;
    font-size: 22px; font-weight: 400;
  }
  .range {
    position: absolute;
    left: 38px; top: 624px;
    list-style: none;
    font-size: 24px; font-weight: 400; line-height: 37px;
  }
  .badge-animal {
    position: absolute;
    left: 583px; top: 599px;
    width: 264px; height: 109px;
    background: var(--green);
    color: var(--white);
    font-size: 24px; font-weight: 600; line-height: 34px;
    padding: 19px 0 0 30px;
  }
  .contact {
    position: absolute;
    left: 38px; top: 796px;
    font-size: 24px; line-height: 35px; font-weight: 400;
    font-style: normal;
  }
  .voucher {
    position: absolute;
    left: 0; top: 940px;
    width: 847px; height: 260px;
    background: var(--green);
    border-top: 3px dashed var(--white);
    overflow: hidden;
  }
  .voucher__pattern {
    position: absolute; inset: 0;
    background:
      radial-gradient(ellipse at 15% 25%, var(--green-soft) 0%, transparent 30%),
      radial-gradient(ellipse at 50% 15%, var(--green-soft) 0%, transparent 28%),
      radial-gradient(ellipse at 85% 25%, var(--green-soft) 0%, transparent 30%),
      radial-gradient(ellipse at 30% 95%, var(--green-light) 0%, transparent 30%),
      radial-gradient(ellipse at 72% 95%, var(--green-light) 0%, transparent 30%);
  }
  .voucher__offer {
    position: absolute;
    left: 0; right: 0; top: 72px;
    text-align: center;
    color: var(--white);
    font-family: "Fredoka", "Open Sans", sans-serif;
    transform: rotate(-7deg);
  }
  .voucher__percent {
    font-size: 74px; font-weight: 600; line-height: 1;
  }
  .voucher__scope {
    margin-top: 6px;
    font-size: 33px; font-weight: 500; line-height: 1.1;
  }
</style>
</head>
<body>
<main class="flyer">
  <header class="brand">
    <div class="brand__name"><span class="brand__dot"></span>QUORVA<br>BLENDS</div>
    <p class="brand__tagline">BE NATURAL WITH QUORVA BLENDS</p>
  </header>

  <div class="product-photo" role="img" aria-label="Foto: handgemachte Seifen- und Badecupcakes in Rosa, Gelb und Creme auf hellem Grund"></div>

  <section class="intro">
    <h1 class="intro__headline">handgefertigt, hochwertig, limitiert.</h1>
    <p class="intro__sub">Beauty &amp; more.</p>
  </section>

  <p class="intro__basis">Basierend auf natürlichen Inhaltsstoffen.</p>

  <ul class="range">
    <li>Badezubehör</li>
    <li>Aromatherapie</li>
    <li>Dekorationsartikel</li>
    <li>Geschenkkörbe</li>
  </ul>

  <div class="badge-animal">NO ANIMAL<br>TESTING</div>

  <address class="contact">
    Mühlgasse 12, 91560 Talheim<br>
    Öffnungszeiten: Freitags 11:00 – 18:00 Uhr<br>
    info@quorvablends.de, www.quorvablends.de
  </address>

  <section class="voucher">
    <div class="voucher__pattern" role="img" aria-label="Dekoratives Muster aus Cupcake-Silhouetten in hellem Grün"></div>
    <div class="voucher__offer">
      <div class="voucher__percent">20%</div>
      <div class="voucher__scope">für Shop &amp;<br>Onlineshop</div>
    </div>
  </section>
</main>
</body>
</html>
```